Family Farm Looking for meat label

We have a small farm in Italy with two types of cow "Piemontese" and "Pezzata Rossa Valdostana". We need label ( about 5x5 cm) to put on the boxes and on every single piece of meat.

Target Market(s)

private client

Industry/Entity Type

family farm

Colors

Designer to choose colors to be used in the design.

Requirements
Must have
• to write "Azienda Agricola Il Mulinetto" and the cow like our cow not differently. the Piemontese breed cow has the typical physical shapes as in the photo. No photo on the label just a drawing o something like that.
Nice to have
• just a one label, clear, fine and clean . Maybe with pastel color or watercolor. We are a small family farm.
Should not have
• no photo, no another type of cow

```html
<!DOCTYPE html>
<html lang="it">
<head>
<meta charset="utf-8">
<title>Il Mulinetto – Meat Label</title>
<link href="https://fonts.googleapis.com/css2?family=Oswald:wght@600&family=Kaushan+Script&family=Quicksand:wght@500&display=swap" rel="stylesheet">
<style>
  :root {
    --backdrop: #d4d4d4;
    --label-white: #ffffff;
    --brand-red: #c8161d;
    --brand-red-dark: #8f0b10;
    --farm-green: #1f9a3e;
    --farm-green-light: #3cb55a;
    --stamp-grey: #8a8a8a;
    --scene-grey: #d6d6d6;
    --scene-grey-soft: #ececec;
  }
  * { margin: 0; padding: 0; box-sizing: border-box; }
  html, body {
    width: 830px;
    height: 1200px;
    overflow: hidden;
    background: var(--backdrop);
  }
  .label {
    position: absolute;
    left: 55px;
    top: 240px;
    width: 720px;
    height: 720px;
    background: var(--label-white);
    overflow: hidden;
    box-shadow: 0 6px 18px rgba(0,0,0,0.25);
  }
  .label__header {
    position: absolute;
    left: 0;
    top: 0;
    width: 720px;
    height: 215px;
  }
  .label__brand {
    position: absolute;
    left: 0;
    width: 720px;
    top: 100px;
    text-align: center;
    font-family: "Oswald", sans-serif;
    font-weight: 600;
    font-size: 46px;
    letter-spacing: 1px;
    color: var(--label-white);
  }
  .label__scene {
    position: absolute;
    left: 0;
    bottom: 0;
    width: 720px;
    height: 240px;
  }
  .label__stamp {
    position: absolute;
    left: 505px;
    top: 215px;
    width: 190px;
    height: 190px;
    border-radius: 50%;
    border: 8px solid var(--stamp-grey);
    box-shadow: inset 0 0 0 6px var(--label-white), inset 0 0 0 9px var(--stamp-grey);
    transform: rotate(15deg);
    display: flex;
    flex-direction: column;
    align-items: center;
    justify-content: center;
    font-family: "Oswald", sans-serif;
    font-weight: 600;
    color: var(--stamp-grey);
    line-height: 1;
  }
  .label__stamp-top { font-size: 34px; }
  .label__stamp-main { font-size: 50px; margin: 2px 0; }
  .label__stamp-bottom { font-size: 22px; }
  .label__title {
    position: absolute;
    font-family: "Kaushan Script", cursive;
    font-size: 118px;
    line-height: 1;
    background: linear-gradient(180deg, var(--farm-green-light), var(--farm-green));
    -webkit-background-clip: text;
    background-clip: text;
    color: transparent;
  }
  .label__title--first { left: 22px; top: 200px; }
  .label__title--second { left: 90px; top: 320px; }
  .label__subtitle {
    position: absolute;
    right: 62px;
    top: 458px;
    font-family: "Quicksand", sans-serif;
    font-weight: 500;
    font-size: 60px;
    line-height: 1;
    color: var(--brand-red);
  }
</style>
</head>
<body>
  <div class="label">
    <svg class="label__scene" viewBox="0 0 720 240" preserveAspectRatio="none" role="img" aria-label="Soft grey sketch of a farm scene with a Piemontese cow, a rooster, a rabbit, a bee and a farmhouse">
      <defs>
        <linearGradient id="sceneTone" x1="0" y1="0" x2="0" y2="1">
          <stop offset="0%" stop-color="#ececec"/>
          <stop offset="100%" stop-color="#d2d2d2"/>
        </linearGradient>
      </defs>
      <path d="M0 40 C60 20 150 10 240 30 C300 45 330 110 420 100 C480 95 520 60 560 50 C620 40 680 60 720 70 V240 H0 Z" fill="url(#sceneTone)"/>
    </svg>

    <svg class="label__header" viewBox="0 0 720 215" aria-hidden="true">
      <defs>
        <radialGradient id="redBand" cx="50%" cy="20%" r="70%">
          <stop offset="0%" stop-color="#e0232a"/>
          <stop offset="100%" stop-color="#8f0b10"/>
        </radialGradient>
      </defs>
      <path d="M0 0 H720 V124 H600 C580 124 575 140 560 155 C520 195 420 205 360 205 C300 205 200 195 160 155 C145 140 140 124 120 124 H0 Z" fill="url(#redBand)"/>
      <path d="M0 128 H118 C138 128 142 144 157 160 C198 200 300 211 360 211 C420 211 522 200 563 160 C578 144 582 128 602 128 H720" fill="none" stroke="#e3e3e3" stroke-width="3"/>
    </svg>
    <div class="label__brand">IL MULINETTO</div>

    <div class="label__stamp">
      <span class="label__stamp-top">La</span>
      <span class="label__stamp-main">qualità</span>
      <span class="label__stamp-bottom">Premium</span>
    </div>

    <div class="label__title label__title--first">Azienda</div>
    <div class="label__title label__title--second">Agricola</div>
    <div class="label__subtitle">Il Mulinetto</div>
  </div>
</body>
</html>
```